A new Velto Speedworks game flyer

Hello.
A few months ago, Kirol made a beautiful flyer for my online Apex Circuit Prime racing league. I would like to make another beautiful flyer but this time for Velto Speedworks. I would like to the design/idea to be very similar except that instead of Apex Circuit Prime, make it called Velto Speedworks. Instead of dark blue, I would like to see mainly white and a bit of red or other colours that go nicely, and a normal fast sports car instead of a Apex Circuit Prime car in the middle. In short - very very similar design/idea to the blue flyer except that I would like it Velto Speedworks themed.

Let me know any questions!

Target Market(s)

Very similar to my current flyer, please follow my instructions in description

Industry/Entity Type

Gaming flyers

Colors
EB3D1F
EC4F4E
F09395
F8D3D4
FCEDEE

Requirements
Must have
• Read above
Nice to have
• As similar design/idea to the flyer i listed
Should not have
• Something completely new and opposite thinking to my flyer

```html
<!DOCTYPE html>
<html lang="en">
<head>
<meta charset="utf-8">
<title>Surge Racing League – Velto Speedworks Flyer</title>
<link href="https://fonts.googleapis.com/css2?family=Oswald:wght@500;600;700&display=swap" rel="stylesheet">
<style>
  :root {
    --page-bg: #e7ebe9;
    --paper: #ffffff;
    --blush: #fcedee;
    --rose: #f8d3d4;
    --pink: #f09395;
    --coral: #ec4f4e;
    --flame: #eb3d1f;
    --flame-deep: #b3130e;
    --ink: #141012;
    --white: #ffffff;
    --silver-hi: #f6f6f6;
    --silver-lo: #a8a8a8;
    --mark-dot: #141012;
  }
  * { margin: 0; padding: 0; box-sizing: border-box; }
  html, body { width: 1200px; height: 800px; overflow: hidden; }
  body {
    background: var(--page-bg);
    font-family: "Oswald", "Arial Narrow", sans-serif;
    position: relative;
  }
  .flyer {
    position: absolute;
    left: 332px; top: 20px;
    width: 535px; height: 760px;
    overflow: hidden;
    background: linear-gradient(180deg, var(--paper) 0%, var(--blush) 45%, var(--rose) 70%, var(--paper) 78%);
    box-shadow: 0 10px 30px rgba(0,0,0,.18);
  }
  .speed-streaks { position: absolute; left: 0; top: 300px; width: 535px; height: 120px; }
  .headline {
    position: absolute; left: 35px; top: 44px; width: 300px;
    color: var(--ink);
    font-weight: 700; font-size: 29px; line-height: 37px;
    text-transform: uppercase; letter-spacing: .3px;
  }
  .headline .brand { color: var(--flame); }
  .league-mark {
    position: absolute; left: 345px; top: 48px; width: 160px;
    text-align: center;
  }
  .league-mark .dot {
    display: block; width: 96px; height: 96px; margin: 0 auto 16px;
    border-radius: 50%; background: var(--flame);
  }
  .league-mark .name {
    color: var(--ink); font-weight: 700; font-size: 28px; line-height: 34px;
    text-transform: uppercase;
  }
  .season-callout { position: absolute; left: 36px; top: 212px; width: 216px; height: 100px; }
  .season-callout svg { position: absolute; inset: 0; }
  .season-callout .text {
    position: absolute; left: 0; top: 10px; width: 208px;
    color: var(--white); font-weight: 600; font-size: 20px; line-height: 26px;
    text-align: center; text-transform: uppercase;
  }
  .crossplay-badge { position: absolute; left: 38px; top: 318px; width: 184px; height: 88px; }
  .crossplay-badge svg { position: absolute; inset: 0; }
  .crossplay-badge .text {
    position: absolute; inset: 0;
    display: flex; align-items: center; justify-content: center; text-align: center;
    color: var(--ink); font-weight: 600; font-size: 16px; line-height: 20px;
    text-transform: uppercase;
  }
  .car-art {
    position: absolute; left: 40px; top: 410px; width: 495px; height: 170px;
    border-radius: 90px 0 0 60px;
    background:
      radial-gradient(ellipse 30% 40% at 82% 30%, rgba(255,200,120,.9), transparent 70%),
      linear-gradient(100deg, #2a3a6a 0%, var(--coral) 35%, var(--flame) 60%, #ff9a3a 85%, var(--flame-deep) 100%);
  }
  .footer-band {
    position: absolute; left: 0; right: 0; top: 600px; bottom: 0;
    background: linear-gradient(180deg, var(--flame) 0%, var(--flame-deep) 100%);
  }
  .friend-banner {
    position: absolute; left: 128px; top: 580px; width: 286px; height: 38px;
    background: var(--ink);
    border: 2px solid var(--white);
    transform: skewX(-14deg);
    display: flex; align-items: center; justify-content: center;
  }
  .friend-banner span {
    transform: skewX(6deg);
    color: var(--white); font-weight: 600; font-size: 19px; font-style: italic;
    text-transform: uppercase;
  }
  .race-times {
    position: absolute; left: 0; right: 0; top: 628px;
    display: flex; align-items: center; justify-content: center; gap: 12px;
    color: var(--white); font-weight: 600; font-size: 20px; text-transform: uppercase;
  }
  .race-times::before, .race-times::after {
    content: ""; width: 46px; height: 2px; background: var(--white);
  }
  .race-days {
    position: absolute; left: 0; right: 0; top: 668px;
    display: flex; justify-content: center; gap: 16px;
  }
  .race-day {
    height: 34px; padding: 0 14px;
    background: linear-gradient(180deg, var(--silver-hi), var(--silver-lo));
    border-left: 4px solid var(--ink);
    transform: skewX(-14deg);
    display: flex; align-items: center; justify-content: center;
  }
  .race-day span {
    transform: skewX(14deg);
    color: var(--ink); font-weight: 600; font-size: 15px; text-transform: uppercase;
  }
  .race-day.mon { width: 102px; }
  .race-day.tue { width: 102px; }
  .race-day.wed { width: 124px; }
  .race-hour {
    position: absolute; left: 0; right: 0; top: 716px;
    text-align: center; color: var(--white);
    font-weight: 600; font-size: 17px; text-transform: uppercase;
  }
</style>
</head>
<body>
  <main class="flyer">
    <svg class="speed-streaks" viewBox="0 0 535 120" aria-hidden="true">
      <line x1="0" y1="30" x2="535" y2="20" stroke="#f09395" stroke-width="3"/>
      <line x1="0" y1="62" x2="535" y2="54" stroke="#ec4f4e" stroke-width="2"/>
      <line x1="0" y1="96" x2="535" y2="90" stroke="#f8d3d4" stroke-width="4"/>
    </svg>

    <h1 class="headline">Very popular, clean<br>and competitive<br><span class="brand">Velto Speedworks</span><br>online racing league</h1>

    <div class="league-mark">
      <span class="dot"></span>
      <p class="name">Surge Racing<br>League</p>
    </div>

    <div class="season-callout">
      <svg width="216" height="100" viewBox="0 0 216 100" aria-hidden="true">
        <polygon points="6,2 214,10 206,74 4,80" fill="none" stroke="#eb3d1f" stroke-width="2"/>
        <polygon points="2,6 208,6 208,72 120,72 110,90 104,72 2,72" fill="#141012"/>
      </svg>
      <p class="text">Running for<br>it's 4th seasons</p>
    </div>

    <div class="crossplay-badge">
      <svg width="184" height="88" viewBox="0 0 184 88" aria-hidden="true">
        <ellipse cx="92" cy="44" rx="89" ry="41" fill="#ffffff" stroke="#eb3d1f" stroke-width="3"/>
      </svg>
      <p class="text">Crossplay/ any<br>platform</p>
    </div>

    <div class="car-art" role="img" aria-label="Fast red sports car racing with light trails and a speedometer dial behind it"></div>

    <div class="footer-band"></div>

    <div class="friend-banner"><span>Why not join with a friend</span></div>

    <p class="race-times">Race times</p>

    <div class="race-days">
      <div class="race-day mon"><span>Mondays</span></div>
      <div class="race-day tue"><span>Tuesdays</span></div>
      <div class="race-day wed"><span>Wednesdays</span></div>
    </div>

    <p class="race-hour">Each at 8pm UK time</p>
  </main>
</body>
</html>
```